Logo and website for new private wealth management business

This project is for a new company website and logo. The name of the firm is Harborline Estate Partners, LLC. We are a wealth management firm offering customized financial planning and investment management services to high net worth and ultra high net worth individuals and families. I want the website to feel contemporary but convey a feeling of sophistication and prestige.
www.tolvanridgeholdings.example and www.qnfunds.example are both good reference websites.
My clients will consist of wealthy individuals and families. I have existing clients in their 50s - 70s, but I also intend to target younger business owners and entrepreneurs in their 30s -50s.

Target Market(s)

Business owners, entrepreneurs and corporate executives. Many existing clients are in their 60s and 70s, but intend to also attract a younger clientele in their 30s - 50s.

Industry/Entity Type

Wealth management, investment advisory, financial planning

Coding

Coded - Design and coding required

Colors
0054AA
0677BA
7BADD7
CADEEF
E8F1F8
0094D4
00A9DD
6FCCEA
C7EBF8
E9F6FB
00AB8E
00BBA5
67D7C9
C6EFE9
E9F9F6
EE7325
F08F49
F5BC92
FAE3D3
FDF4ED

Requirements
Must have
• Should use blue as the main color theme. Should have an About, Services, Our Clients, FAQ, and Contact sections
Should not have
• Should not have pictures of people as the background.

```html
<!DOCTYPE html>
<html lang="en">
<head>
<meta charset="utf-8">
<title>Harborline Estate Partners, LLC</title>
<link rel="stylesheet" href="https://fonts.googleapis.com/css2?family=Lexend:wght@400;500;600;700;800&family=Arimo:wght@400;700&display=swap">
<style>
:root{
  --navy:#0a1730;
  --navy-deep:#06112a;
  --primary:#0e3f86;
  --primary-dark:#0b3270;
  --accent:#0094d4;
  --accent-light:#00a9dd;
  --teal:#00bba5;
  --ink:#111827;
  --body:#3a3f4a;
  --muted:#c9ccd2;
  --faq-bg:#f4f6fa;
  --white:#ffffff;
  --line:#cfd6e2;
}
*{box-sizing:border-box;margin:0;padding:0}
html,body{width:1200px;height:5088px;overflow:hidden;background:var(--white)}
body{position:relative;font-family:"Arimo",Arial,sans-serif;color:var(--body)}
.abs{position:absolute}
.heading{font-family:"Lexend",Arial,sans-serif;font-weight:700;color:var(--primary)}
.btn{position:absolute;display:flex;align-items:center;justify-content:center;background:var(--primary);color:var(--white);font-family:"Lexend",Arial,sans-serif;font-weight:600;font-size:15px;letter-spacing:.5px}

/* hero */
.hero{position:absolute;left:0;top:0;width:1200px;height:760px;background:linear-gradient(180deg,#081428 0%,#0b1c3c 100%);overflow:hidden}
.hero-art{position:absolute;left:560px;top:80px;width:640px;height:600px;background:radial-gradient(ellipse at 55% 50%,#1d6fa8 0%,#123f74 30%,#0b2146 60%,rgba(8,20,40,0) 80%)}
.brand{position:absolute;left:99px;top:30px;color:var(--white);font-family:"Lexend",Arial,sans-serif}
.brand b{display:block;font-size:32px;font-weight:800;letter-spacing:1px;line-height:34px}
.brand span{display:block;font-size:13px;font-weight:600;letter-spacing:1.2px}
.nav{position:absolute;top:38px;left:478px;display:flex;gap:0;align-items:center;font-family:"Lexend",Arial,sans-serif;font-weight:600;font-size:15px;color:var(--white);letter-spacing:.6px}
.nav a{color:inherit;text-decoration:none;margin-right:52px}
.nav .nav-cta{margin:0;background:var(--primary);padding:12px 24px;margin-left:-4px}
.hero-title{position:absolute;left:96px;top:210px;font-family:"Lexend",Arial,sans-serif;font-weight:700;font-size:58px;line-height:68px;color:var(--white)}
.hero-text{position:absolute;left:99px;top:370px;width:540px;font-size:16px;line-height:26px;color:var(--white)}

/* about */
.side-word{position:absolute;font-family:"Lexend",Arial,sans-serif;font-weight:800;color:#c5c8ce;transform-origin:left top;transform:rotate(-90deg);white-space:nowrap}
.about-image{position:absolute;left:193px;top:875px;width:387px;height:388px;border-radius:18px;background:linear-gradient(180deg,#0e7f83 0%,#18b59c 60%,#3ee0b8 100%)}
.label{font-family:"Lexend",Arial,sans-serif;font-weight:600;font-size:20px;letter-spacing:3px;color:var(--ink)}
.para{font-size:16px;line-height:26px;color:var(--body)}

/* why choose */
.why-item{position:absolute;width:230px}
.why-item h3{font-family:"Lexend",Arial,sans-serif;font-weight:600;font-size:21px;color:var(--ink);margin-bottom:10px}
.why-item p{font-size:15px;line-height:25px;color:var(--body)}
.why-item.left{text-align:right}

/* services */
.svc-card{position:absolute;width:263px;height:213px;border-radius:14px;background:var(--white);box-shadow:0 6px 30px rgba(15,40,90,.10);display:flex;flex-direction:column;align-items:center;justify-content:flex-end;padding-bottom:38px;text-align:center;font-family:"Lexend",Arial,sans-serif;font-weight:600;font-size:21px;line-height:31px;color:var(--ink)}
.svc-card svg{margin-bottom:14px}
.svc-card.active{background:var(--primary);color:var(--white)}

/* clients */
.client{position:absolute;width:170px;height:130px;display:flex;flex-direction:column;align-items:center;justify-content:flex-end;font-family:"Lexend",Arial,sans-serif;font-weight:600;font-size:22px;color:var(--primary)}
.client i{display:block;width:64px;height:64px;border-radius:50%;background:#d9e7f5;margin-bottom:14px}

/* faq */
.faq{position:absolute;left:0;top:3395px;width:1200px;height:622px;background:var(--faq-bg)}
.faq-item{position:absolute;left:213px;font-size:17px;color:var(--ink)}
.faq-item::before{content:"";position:absolute;left:-26px;top:7px;width:7px;height:7px;border-radius:50%;background:var(--primary)}
.faq-item.open{font-weight:700}
.faq-item.open::before{left:-31px;top:2px;width:17px;height:17px}
.faq-answer{position:absolute;left:213px;top:3743px;width:810px;font-size:15px;line-height:24px;color:var(--body)}

/* contact */
.contact{position:absolute;left:0;top:4017px;width:1200px;height:660px;background:linear-gradient(180deg,#0a1730 0%,#0d1f3f 60%,#0a1730 100%)}
.contact-info{position:absolute;left:99px;color:var(--white);font-size:16px;line-height:26px}
.contact-info svg{position:absolute;left:0;top:3px}
.contact-info span{display:block;padding-left:34px}
.form{position:absolute;left:527px;top:4082px;width:573px;height:389px;background:var(--white);border-radius:20px}
.field{position:absolute;border:1px solid #9aa3b2;font-size:15px;color:var(--ink);padding:10px 10px}

/* footer */
.foot-col h4{font-family:"Lexend",Arial,sans-serif;font-weight:600;font-size:21px;color:var(--primary);margin-bottom:18px}
.foot-col a{display:block;font-size:15px;color:var(--body);text-decoration:none;margin-bottom:23px}
.social{position:absolute;top:4840px;width:34px;height:34px;border-radius:50%;background:var(--primary)}
</style>
</head>
<body>

<!-- HERO -->
<section class="hero">
  <div class="hero-art" role="img" aria-label="Digital globe rising above stacks of coins with glowing light streaks"></div>
  <div class="brand"><b>HARBORLINE</b><span>ESTATE PARTNERS, LLC.</span></div>
  <nav class="nav">
    <a href="#about">ABOUT</a><a href="#services">SERVICES</a><a href="#clients">OUR CLIENTS</a><a href="#faq">FAQ</a><a class="nav-cta" href="#contact">CONTACT US</a>
  </nav>
  <h1 class="hero-title">Customized<br>Financial Planning</h1>
  <p class="hero-text">Suspendisse vehicula commodo sodales. Lorem ipsum dolor sit amet, consectetur adipiscing elit. Morbi lorem elit, viverra sit amet ligula nec</p>
  <a class="btn" style="left:99px;top:478px;width:173px;height:51px">KNOW MORE</a>
  <svg class="abs" style="left:0;top:600px" width="1200" height="162" viewBox="0 0 1200 162">
    <path d="M0 40 C300 150 800 150 1200 40 L1200 162 L0 162Z" fill="#0e3f86"/>
    <path d="M0 40 C300 130 800 110 1200 55 L1200 70 C800 120 330 150 0 62Z" fill="#0094d4" opacity=".5"/>
    <path d="M0 62 C330 150 800 135 1200 70 L1200 162 L0 162Z" fill="#ffffff"/>
    <rect x="590" y="52" width="20" height="30" rx="10" fill="none" stroke="#fff" stroke-width="2"/>
    <line x1="600" y1="59" x2="600" y2="66" stroke="#fff" stroke-width="2"/>
  </svg>
</section>

<!-- ABOUT -->
<section id="about">
  <div class="side-word" style="left:92px;top:1245px;font-size:92px">ABOUT</div>
  <div class="about-image" role="img" aria-label="Teal financial chart with rising bars over a city skyline"></div>
  <div class="abs label" style="left:614px;top:870px">ABOUT</div>
  <h2 class="abs heading" style="left:614px;top:895px;font-size:56px;line-height:64px;width:560px">Harborline Estate<br>Partners, LLC.</h2>
  <p class="abs para" style="left:612px;top:1044px;width:486px">Lorem ipsum dolor sit amet, consectetur adipiscing elit. Aenean tristique arcu eget leo effir faucibus. Integer maximus est non leo pellentesque gravida. Suspendisse facilisis ac sem non iaculis. Suspendisse vehicula commodo sodales. Lorem ipsum dolor sit amet, consectetur adipiscing elit.</p>
  <a class="btn" style="left:610px;top:1212px;width:173px;height:51px">READ MORE</a>
</section>

<!-- WHY CHOOSE US -->
<section>
  <h2 class="abs heading" style="left:0;width:1200px;text-align:center;top:1432px;font-size:56px">Why Choose Us</h2>
  <svg class="abs" style="left:0;top:1540px" width="1200" height="520" viewBox="0 0 1200 520">
    <!-- connector lines -->
    <g fill="none" stroke="#0b3270" stroke-width="3">
      <path d="M99 224 H330 Q345 224 350 200 L372 108"/>
      <path d="M99 296 H330 Q345 296 350 320 L372 405"/>
    </g>
    <g fill="none" stroke="#0094d4" stroke-width="3">
      <path d="M1101 224 H870 Q855 224 850 200 L828 108"/>
      <path d="M1101 296 H870 Q855 296 850 320 L828 405"/>
    </g>
    <g fill="#fff" stroke="#0b3270" stroke-width="3">
      <circle cx="374" cy="106" r="10"/><circle cx="374" cy="408" r="10"/>
      <circle cx="826" cy="106" r="10"/><circle cx="826" cy="408" r="10"/>
    </g>
    <!-- rings -->
    <path d="M600 28 A232 232 0 0 0 600 492" fill="none" stroke="#0b2a5c" stroke-width="34"/>
    <path d="M600 28 A232 232 0 0 1 832 260" fill="none" stroke="#0094d4" stroke-width="34"/>
    <path d="M832 260 A232 232 0 0 1 600 492" fill="none" stroke="#0e3f86" stroke-width="34"/>
    <line x1="600" y1="0" x2="600" y2="520" stroke="#ffffff" stroke-width="3"/>
    <circle cx="600" cy="260" r="180" fill="none" stroke="#0e3f86" stroke-width="3"/>
    <path d="M575 82 l14 -7 -4 14" fill="none" stroke="#0e3f86" stroke-width="3"/>
    <path d="M770 250 l8 14 8 -14" fill="none" stroke="#0e3f86" stroke-width="3"/>
    <path d="M625 438 l-14 7 4 -14" fill="none" stroke="#0e3f86" stroke-width="3"/>
    <path d="M430 270 l-8 -14 -8 14" fill="none" stroke="#0e3f86" stroke-width="3"/>
    <!-- icons -->
    <g fill="none" stroke="#0b3270" stroke-width="2.5">
      <rect x="280" y="-2" width="44" height="52" rx="3"/><rect x="292" y="-8" width="20" height="10"/>
      <path d="M290 14 l4 4 8 -8 M290 28 l4 4 8 -8 M290 42 h24"/>
      <rect x="268" y="342" width="52" height="32" rx="4"/><path d="M280 342 v-14 h24 v14 M294 352 v16"/>
    </g>
    <g fill="none" stroke="#0094d4" stroke-width="2.5">
      <circle cx="896" cy="20" r="24"/><circle cx="896" cy="20" r="9"/>
      <circle cx="880" cy="330" r="10"/><circle cx="914" cy="330" r="10"/><circle cx="880" cy="362" r="10"/><circle cx="914" cy="362" r="10"/>
    </g>
  </svg>
  <div class="abs" role="img" aria-label="Money bag, coins, calculator and rising red arrow illustration" style="left:480px;top:1720px;width:240px;height:150px;border-radius:50%;background:radial-gradient(ellipse,#3d6fb0 0%,#e9f1f8 70%,rgba(255,255,255,0) 72%)"></div>
  <div class="why-item left" style="left:98px;top:1605px"><h3>Financial planning</h3><p>Suspendisse facilisis ac sem non iaculis. Suspisse vehicula commodo sodales.</p></div>
  <div class="why-item" style="left:871px;top:1605px"><h3>Management</h3><p>Suspendisse facilisis ac sem non iaculis. Suspisse vehicula commodo sodales.</p></div>
  <div class="why-item left" style="left:98px;top:1925px"><h3>Investment</h3><p>Suspendisse facilisis ac sem non iaculis. Suspisse vehicula commodo sodales.</p></div>
  <div class="why-item" style="left:870px;top:1925px"><h3>Resources</h3><p>Suspendisse facilisis ac sem non iaculis. Suspisse vehicula commodo sodales.</p></div>
</section>

<!-- SERVICES -->
<section id="services">
  <h2 class="abs heading" style="left:99px;top:2275px;font-size:56px;line-height:62px">Our<br>Services</h2>
  <p class="abs para" style="left:99px;top:2420px;width:335px;font-size:15px;line-height:25.5px">Phasellus eu rutrum lectus, sed tincidunt metus. Pellentesque nisl mi, tincidunt quis quam scelerisque, ullamcorper laoreet nisi. Pesent facisis vitae velit eget scelerisque. Maecenas sagitlamcorper ante ac efficitur. Phasellus volutpat eget arcu non ornare. Aliquam erat volpat. Donec eu est volutpat nisi blandit venenatis.</p>
  <a class="btn" style="left:99px;top:2657px;width:225px;height:53px">VIEW ALL SERVICES</a>
  <div class="svc-card active" style="left:499px;top:2286px">
    <svg width="76" height="70" viewBox="0 0 76 70" fill="none" stroke="#fff" stroke-width="2.5"><rect x="4" y="10" width="46" height="56" rx="3"/><rect x="30" y="26" width="34" height="40" rx="3"/><path d="M36 36h22M36 46h6M46 46h6M56 46h2M36 56h6M46 56h6"/><circle cx="62" cy="12" r="9"/></svg>
    Customized<br>Financial Planning
  </div>
  <div class="svc-card" style="left:805px;top:2286px">
    <svg width="76" height="70" viewBox="0 0 76 70" fill="none" stroke="#0e3f86" stroke-width="2.5"><path d="M6 64h64M12 64V42h10v22M30 64V32h10v22M48 64V22h10v42M10 30 L34 16 48 22 66 6"/><circle cx="54" cy="50" r="12"/></svg>
    Investment<br>Management
  </div>
  <div class="svc-card" style="left:651px;top:2535px">
    <svg width="76" height="70" viewBox="0 0 76 70" fill="none" stroke="#0e3f86" stroke-width="2.5"><circle cx="40" cy="16" r="13"/><path d="M4 52 l14 -10 h22 a5 5 0 0 1 0 10 H28 M40 50 l20 -10 a5 5 0 0 1 6 8 L40 66 H16 L8 60"/></svg>
    Other Financial<br>Service
  </div>
  <div class="side-word" style="left:1110px;top:2843px;font-size:92px">SERVICES</div>
</section>

<!-- CLIENTS -->
<section id="clients">
  <h2 class="abs heading" style="left:0;width:1200px;text-align:center;top:2890px;font-size:56px">Our Clients</h2>
  <div class="client" style="left:83px;top:3000px"><i></i>Ledgerly</div>
  <div class="client" style="left:255px;top:3000px"><i></i>Quillmark</div>
  <div class="client" style="left:438px;top:3000px"><i></i>Baseworks</div>
  <div class="client" style="left:615px;top:3000px"><i></i>Nova Nine</div>
  <div class="client" style="left:793px;top:3000px"><i></i>Clearsight</div>
  <div class="client" style="left:961px;top:3000px"><i></i>Upcurve</div>
  <div class="client" style="left:83px;top:3198px"><i></i>Formline</div>
  <div class="client" style="left:255px;top:3198px"><i></i>K.T. Mark</div>
  <div class="client" style="left:438px;top:3198px"><i></i>Facetra</div>
  <div class="client" style="left:615px;top:3198px"><i></i>Mediarc</div>
  <div class="client" style="left:793px;top:3198px"><i></i>Thinkwell</div>
  <div class="client" style="left:961px;top:3198px"><i></i>Prismix</div>
</section>

<!-- FAQ -->
<section id="faq" class="faq"></section>
<div class="abs" style="left:0;width:1200px;text-align:center;top:3466px;font-family:'Lexend',Arial,sans-serif;font-weight:600;font-size:22px;color:var(--ink)">Frequently</div>
<h2 class="abs heading" style="left:0;width:1200px;text-align:center;top:3497px;font-size:56px">Asked Questions</h2>
<div class="faq-item" style="top:3598px">Lorem ipsum dolor sit amet, consectetur adipiscing elit?</div>
<div class="faq-item" style="top:3650px">Aenean tristique arcu eget leo efficitur faucibhasellus eu rutrum lectus?</div>
<div class="faq-item open" style="top:3701px">Integer maximus est non leo pellentesque gravida?</div>
<div class="abs" style="left:196px;top:3742px;width:2px;height:56px;background:var(--primary)"></div>
<p class="faq-answer">Lorem ipsum dolor sit amet, consectetur adipiscict. Aenean tristique arcu eget leo efficitur faucibus. Inter maximus est non leo pellentesque gravida. Suspendisse facilisis ac sem non iaculis. Suspndisse vehicula commodo sodales. Lorem ipsum dolor sit amet</p>
<div class="faq-item" style="top:3835px">Pellentesque nisl, tiniduuis quam scelerisque, ullamcorper laoreesent facilisis vitae velit eget?</div>
<div class="faq-item" style="top:3879px">Aenean tristique arcu eget leo efficitur faucibhasellus eu rutrum lectus?</div>

<!-- CONTACT -->
<section id="contact" class="contact" role="img" aria-label="Dark blue mountain landscape backdrop"></section>
<h2 class="abs heading" style="left:97px;top:4185px;font-size:56px;color:var(--white)">Contact Us</h2>
<div class="contact-info" style="top:4248px">
  <svg width="22" height="24" viewBox="0 0 22 24" fill="none" stroke="#fff" stroke-width="2"><path d="M11 20 C4 12 4 10 4 8 a7 7 0 0 1 14 0 c0 2 0 4 -7 12Z"/><circle cx="11" cy="8" r="2.5"/><ellipse cx="11" cy="21" rx="9" ry="2"/></svg>
  <span>418 Tidewater Lane<br>Port Alden, CA 90210</span>
</div>
<div class="contact-info" style="top:4320px">
  <svg width="22" height="18" viewBox="0 0 22 18" fill="none" stroke="#fff" stroke-width="2"><rect x="1" y="2" width="20" height="14"/><path d="M1 2 l10 8 10 -8"/></svg>
  <span>info@harborlineestate.example</span>
</div>
<div class="contact-info" style="top:4362px">
  <svg width="22" height="22" viewBox="0 0 22 22" fill="none" stroke="#fff" stroke-width="2"><path d="M5 2 l4 5 -2 3 c1 2 3 4 5 5 l3 -2 5 4 -3 3 C10 20 2 12 2 5Z"/></svg>
  <span>(555)-010-2741</span>
</div>
<div class="form">
  <h3 class="abs heading" style="left:26px;top:22px;font-size:32px;color:var(--primary)">Get In Touch</h3>
  <div class="field" style="left:24px;top:76px;width:258px;height:44px">Name</div>
  <div class="field" style="left:292px;top:76px;width:258px;height:44px">Email</div>
  <div class="field" style="left:24px;top:132px;width:258px;height:44px">Phone</div>
  <div class="field" style="left:292px;top:132px;width:258px;height:44px">Subject</div>
  <div class="field" style="left:24px;top:188px;width:526px;height:102px">Your Message</div>
  <a class="btn" style="left:24px;top:302px;width:171px;height:51px">SUBMIT NOW</a>
</div>

<!-- FOOTER WAVE -->
<svg class="abs" style="left:0;top:4530px" width="1200" height="160" viewBox="0 0 1200 160">
  <path d="M0 40 C300 140 850 140 1200 70 L1200 160 L0 160Z" fill="#0e3f86"/>
  <path d="M0 80 C320 150 850 150 1200 95 L1200 160 L0 160Z" fill="#ffffff"/>
  <path d="M0 72 C320 142 850 142 1200 88" fill="none" stroke="#0094d4" stroke-width="4" opacity=".6"/>
</svg>

<!-- FOOTER -->
<footer>
  <div class="abs" style="left:99px;top:4718px;font-family:'Lexend',Arial,sans-serif;color:var(--primary)">
    <b style="display:block;font-size:32px;font-weight:800;letter-spacing:1px;line-height:34px">HARBORLINE</b>
    <span style="display:block;font-size:13px;font-weight:600;letter-spacing:1.2px">ESTATE PARTNERS, LLC.</span>
  </div>
  <span class="social" style="left:106px"></span>
  <span class="social" style="left:154px"></span>
  <span class="social" style="left:201px"></span>
  <span class="social" style="left:248px"></span>
  <div class="abs foot-col" style="left:346px;top:4716px"><h4>Quick Links</h4><a>About</a><a>Services</a><a>Our Clients</a><a>FAQ</a><a>Contact Us</a></div>
  <div class="abs foot-col" style="left:544px;top:4716px"><h4>Services</h4><a>Customized Financial Planning</a><a>Investment Management</a><a>Other Financial Service</a></div>
  <div class="abs foot-col" style="left:839px;top:4716px"><h4>Newsletter</h4></div>
  <div class="field" style="left:839px;top:4770px;width:262px;height:52px;border-color:#9aa3b2;color:var(--body);padding:16px 12px 0 34px">Enter email address</div>
  <svg class="abs" style="left:849px;top:4790px" width="16" height="12" viewBox="0 0 16 12" fill="none" stroke="#6b7280" stroke-width="1.5"><rect x="1" y="1" width="14" height="10"/><path d="M1 1 l7 5 7 -5"/></svg>
  <a class="btn" style="left:839px;top:4840px;width:171px;height:51px">SUBSCRIBE</a>
  <div class="abs" style="left:99px;top:5030px;font-size:12px;color:var(--ink)">© 2022 <b style="color:var(--primary)">Harborline Estate Partners, LLC.</b> All right reserved</div>
  <div class="abs" style="left:478px;top:5038px;width:470px;height:1px;background:var(--primary)"></div>
</footer>

</body>
</html>
```